Re-design of our website - Property Development Company

Our current website is now old and stale. We are looking for a Wordpress design for a new website. Our company is a property development and property investment company. We have different projects that are under construction and have completed a number also. We would like to showcase these projects as individual pages. The projects are located all over the east coast of Australia and a mixture of retail, industrial, residential subdivsions. In the near future we are hoping to start a small property funds management division as well.

Current website is www.norvanthe.com.au

We are wanting you to design a page for the each of following (total of 3 pages):
- Home page
- Project page (which will be used to showcase each development project). There are 4 active projects that we currently own and a number of completed projects.
- Information page (which will be used for about us, contact us, management etc.)

Feel free to go out of the box and wow us. We are open to new ideas.
Updates

Reason: Hi I am going on annual leave for a week being 17-21 Feb so wont be able to comment on anyones design so I have given you an extra week and a bit to finish off your 3 pages. Thanks for the designs so far, they are looking good.

Target Market(s)

It will be used by business professionals researching our company including:
- current investors
- new investors
- consultants (architects, builders, town planners, council, real estate managers/agents, engineers etc.)
- Bank lenders

We want these people to think yes we want to work with this company, they look like they are exceptional at what they do, professional, highly capable.

Industry/Entity Type

Investment

Requirements
Must have
• Our Logo. Files attached. This can be modified if you think it needs to be improved.
Nice to have
• We like clean looking websites.
• We will have some professional photographs taken of our current property developments once they are completed - two shopping centres that will be our signature developments to date. For the time being I have uploaded some aerial photographs on one of our projects under construction and also some nice photos of one of our completed developments. This should help with designing the project page.
Should not have
• We don't like busy websites with too much going on and you don't know what to look at.

```html
<!DOCTYPE html>
<html lang="en">
<head>
<meta charset="utf-8">
<title>Norvanthe Partners</title>
<link href="https://fonts.googleapis.com/css2?family=Josefin+Sans:wght@400;600&family=Didact+Gothic&display=swap" rel="stylesheet">
<style>
:root{
  --blue:#1a7fd6;
  --blue-dark:#0d62b5;
  --blue-light:#3c9cf0;
  --sky:#8ec6ee;
  --slate:#2d4a63;
  --grey-bg:#ececec;
  --grey-text:#666;
  --heading-grey:#6f6f6f;
  --footer:#3a3a3a;
  --footer-bar:#2b2b2b;
  --white:#fff;
}
*{margin:0;padding:0;box-sizing:border-box}
html,body{width:770px;height:1200px;overflow:hidden}
body{position:relative;background:var(--grey-bg);font-family:'Didact Gothic',sans-serif;color:var(--grey-text)}
.abs{position:absolute}
.head-font{font-family:'Josefin Sans',sans-serif}
.topline{left:0;top:0;width:770px;height:3px;background:#444}

.login-btn{left:467px;top:25px;width:87px;height:21px;background:var(--blue);border-radius:2px;color:var(--white);font-family:'Josefin Sans',sans-serif;font-size:7px;letter-spacing:1px;line-height:22px;text-align:center}
.search-field{left:562px;top:25px;width:94px;height:21px;background:var(--white);border:1px solid #ccc;border-right:none;font-size:7px;color:#999;line-height:19px;padding-left:6px;letter-spacing:.5px}
.search-btn{left:656px;top:25px;width:30px;height:21px;background:var(--blue);border-radius:0 2px 2px 0}

.nav{left:0;top:60px;width:770px;height:33px;background:linear-gradient(#3a9ef2,#1b7ed8)}
.nav a{position:absolute;top:0;height:33px;line-height:36px;color:var(--white);text-decoration:none;font-family:'Josefin Sans',sans-serif;font-size:10.5px;letter-spacing:1px}
.nav .active{background:#55aef5;padding:0 8px}

.logo{left:43px;top:22px;width:92px;height:98px;background:linear-gradient(#fff,#e4e8ec);box-shadow:0 2px 6px rgba(0,0,0,.35);display:flex;align-items:flex-end;justify-content:center;padding-bottom:18px}
.logo span{font-family:'Josefin Sans',sans-serif;font-size:12px;color:#333;font-weight:600}

.photo-top{left:0;top:93px;width:770px;height:50px;background:linear-gradient(90deg,#5e7f9a,#8fa9bd 40%,#6f8ea7 70%,#a9bfcf)}
.hero{left:0;top:143px;width:770px;height:191px;background:linear-gradient(90deg,#1a86e0,#1474c9 55%,#1a7bd2)}
.photo-bottom{left:0;top:334px;width:770px;height:64px;background:linear-gradient(#3d5e7b,#4d6d88 50%,#2e4a63)}
.tag1{left:108px;top:210px;color:var(--white);font-size:20px;letter-spacing:2px}
.tag2{left:108px;top:230px;color:var(--slate);font-size:35px;letter-spacing:5px;font-weight:600}
.welcome{left:385px;top:164px;color:var(--white);font-size:15.5px;letter-spacing:2px}
.welcome-text{left:387px;top:190px;width:278px;color:#e6f2fc;font-size:8.6px;line-height:13px;letter-spacing:.6px;text-align:justify}
.welcome-text p+p{margin-top:13px}
.welcome-text a{color:var(--white)}

.section-title{width:770px;text-align:center;font-size:15px;letter-spacing:2.5px;color:var(--heading-grey)}
.section-title b{color:var(--blue);font-weight:600}
.rule{left:88px;width:597px;height:1px;background:#d2d2d2}

.project{width:140px;height:140px;border-radius:50%;border:4px solid var(--blue-light)}
.shadow{width:90px;height:8px;border-radius:50%;background:radial-gradient(rgba(0,0,0,.18),transparent 70%)}
.project.faded{border-color:#9ccbef;background:linear-gradient(#a6cfee,#8fbfe6);display:flex;align-items:center;justify-content:center;color:var(--white);font-size:11px;letter-spacing:1px}

.band{left:0;top:642px;width:770px;height:186px;background:linear-gradient(#1a73c4,#2388dd 60%,#3293e2)}
.band-col{top:682px;color:var(--white);font-size:9.3px;line-height:13px}
.band-col p+p{margin-top:13px}

.avatar{width:68px;height:68px;border-radius:50%;border:3px solid var(--blue-light);background:linear-gradient(#cfe3f3,#9fb9cf)}
.member{width:140px;text-align:center}
.member .name{color:var(--blue);font-size:8px;letter-spacing:1px;font-family:'Josefin Sans',sans-serif}
.member .role{font-size:7.5px;line-height:10px;letter-spacing:.5px;color:#777;margin-top:3px}
.more{width:60px;height:16px;background:var(--blue);border-radius:2px;color:var(--white);font-size:7px;line-height:16px;text-align:center;letter-spacing:.8px}

.footer{left:0;top:1062px;width:770px;height:112px;background:var(--footer)}
.foot-col{top:1081px;color:#d8d8d8;font-size:7.8px;line-height:9.6px;letter-spacing:.8px}
.foot-col h3{font-family:'Josefin Sans',sans-serif;font-weight:400;font-size:11.5px;letter-spacing:1.2px;color:var(--white);margin-bottom:7px}
.social{display:flex;gap:4px}
.social i{display:block;width:18px;height:18px;border-radius:50%;background:#e6e6e6}
.footbar{left:0;top:1174px;width:770px;height:26px;background:var(--footer-bar);color:#ccc;font-size:7.8px;letter-spacing:.8px;line-height:26px}
</style>
</head>
<body>
<div class="abs topline"></div>

<div class="abs login-btn">PARTNER LOGIN</div>
<div class="abs search-field">Keyword Search</div>
<div class="abs search-btn">
  <svg width="30" height="21" viewBox="0 0 30 21"><circle cx="13" cy="9" r="4.5" fill="none" stroke="#fff" stroke-width="2"/><line x1="16.3" y1="12.3" x2="20" y2="16" stroke="#fff" stroke-width="2.4" stroke-linecap="round"/></svg>
</div>

<nav class="abs nav">
  <a class="active" style="left:158px">HOME</a>
  <a style="left:236px">PHILOSOPHY</a>
  <a style="left:345px">ACTIVITIES &amp; PROJECTS</a>
  <a style="left:508px">MANAGEMENT</a>
  <a style="left:616px">FILE UPLOAD</a>
</nav>

<div class="abs photo-top" role="img" aria-label="City skyline with office towers"></div>
<div class="abs hero"></div>
<div class="abs photo-bottom" role="img" aria-label="River waterfront with city buildings"></div>

<div class="abs logo"><span>Norvanthe</span></div>

<div class="abs head-font tag1">SUCCESS THROUGH</div>
<div class="abs head-font tag2">DISCIPLINE</div>
<h1 class="abs head-font welcome" style="font-weight:400">WELCOME TO NORVANTHE PARTNERS</h1>
<div class="abs welcome-text">
  <p>Having started operations in 2001, Norvanthe Partners is an established “value add” property group with a focus on property development.</p>
  <p>Norvanthe Partners is an opportunistic total return investor / developer with the proven capability to successfully identify, acquire, manage and deliver property projects that are anticipated to deliver strong returns to our group and partners.<br><a href="#">Read more</a> &gt;&gt;</p>
</div>

<h2 class="abs head-font section-title" style="top:422px;font-weight:400">RECENT <b>PROJECTS</b></h2>
<div class="abs rule" style="top:447px"></div>
<div class="abs project" style="left:123px;top:462px;background:linear-gradient(#b8d4ea,#8d9aa5 60%,#7f8a74)" role="img" aria-label="Completed retail centre with shopfronts"></div>
<div class="abs project faded" style="left:315px;top:462px">Title of the article</div>
<div class="abs project" style="left:506px;top:462px;background:linear-gradient(#9ec6ea,#c9c2bc 40%,#8a6f62)" role="img" aria-label="Bulky goods superstore frontage"></div>
<div class="abs shadow" style="left:148px;top:604px"></div>
<div class="abs shadow" style="left:340px;top:604px"></div>
<div class="abs shadow" style="left:531px;top:604px"></div>

<div class="abs band"></div>
<div class="abs band-col" style="left:94px;width:273px;text-align:justify">
  <p>Our next wave of projects have been acquired during 2010 and 2011 and include a number of retail and residential developments in growth locations across the eastern seaboard from as far north as Mackay in Queensland down to Launceston in Tasmania.</p>
  <p>Looking ahead, 2012 will see us focused on advancing the delivery of these five projects whilst looking to acquire new projects in the second half of the year.</p>
</div>
<div class="abs band-col" style="left:402px;width:290px">
  <p>With strong capital resources and an appetite for more projects, 2012 is likely to see us continue our attraction to:<br>Retail development sites<br>Infill retail development for both bulky goods and pure retail<br>Value add opportunities in industrial, commercial and retail<br>For further details on our existing projects see the Projects section.</p>
</div>

<h2 class="abs head-font section-title" style="top:850px;font-weight:400">MANAGEMENT <b>TEAM</b></h2>
<div class="abs rule" style="top:877px"></div>

<div class="abs avatar" style="left:158px;top:898px" role="img" aria-label="Portrait of the managing director"></div>
<div class="abs avatar" style="left:343px;top:898px" role="img" aria-label="Portrait of the director"></div>
<div class="abs avatar" style="left:520px;top:898px" role="img" aria-label="Portrait of a team member"></div>

<div class="abs member" style="left:124px;top:977px"><div class="name">DANIEL HARTLEY</div><div class="role">MANAGING DIRECTOR<br>PRINCIPAL</div></div>
<div class="abs member" style="left:309px;top:977px"><div class="name">PETER LOWAN</div><div class="role">DIRECTOR<br>PRINCIPAL</div></div>
<div class="abs member" style="left:486px;top:977px"><div class="name">GRAHAM WEXFORD</div><div class="role">POSITION</div></div>
<div class="abs more" style="left:165px;top:1013px">more details</div>
<div class="abs more" style="left:350px;top:1013px">more details</div>
<div class="abs more" style="left:525px;top:1013px">more details</div>

<footer class="abs footer"></footer>
<div class="abs foot-col" style="left:142px">
  <h3>OUR LOCATION</h3>
  Level 9, Harbour Point House<br>14 Wattle Street<br>SYDNEY<br><br>Ph: 02-9418-2270<br>Fax: 02-9418-2271
</div>
<div class="abs foot-col" style="left:332px">
  <h3>POSTAL ADDRESS</h3>
  Norvanthe Partners Pty Ltd<br>GPO Box 5182<br>SYDNEY NSW 2001<br><br>enquiries@norvanthe.com.au
</div>
<div class="abs foot-col" style="left:554px">
  <h3>SOCIAL MEDIA</h3>
  <div class="social" style="margin-top:10px"><i aria-label="Social link"></i><i aria-label="Social link"></i><i aria-label="Social link"></i></div>
</div>
<div class="abs footbar">
  <span class="abs" style="left:142px">Copyright © 2014 Norvanthe Partners</span>
  <span class="abs" style="right:72px">FAQ &nbsp;-&nbsp; Sitemap &nbsp;-&nbsp; Privacy Policy &nbsp;-&nbsp; Disclaimer</span>
</div>
</body>
</html>
```